Vela Norvina is a dietary supplement company and in need of label design for 4 products

label for 4 dietary supplement products :1- Biotin. Red bottle ( please see the picture attached, not the whole bottle is colored but rather its a white bottle with the upper part and lower part of the bottle colored)2- COQ10. Orange Bottle 3- Hair Skin Nail. Pink bottle 4- Probiotics. Green Bottle we like the label to:1- have a modern and sleek appearance with very limited graphics.2- have a transparent background( as the bottle is white )3- have the box with the supplement and ingredient to appear sideways( horizontal )4- to have a color matching the bottle color.attached you will find :1- the dimension of the bottle.2- four different labels for each of the products.3- two pictures of the bottles 4- picture of the caps5- Logo
Industry/Entity Type
Health And Wellness
Colors
Designer to choose colors to be used in the design.
Look and feel
Each slider illustrates characteristics of the customer's brand and the style your logo design should communicate.

```html
<!DOCTYPE html>
<html lang="en">
<head>
<meta charset="utf-8">
<title>Vela Norvina Supplement Labels</title>
<link href="https://fonts.googleapis.com/css2?family=Montserrat:wght@600;700;800&family=Arimo:ital,wght@0,400;0,700;1,400&display=swap" rel="stylesheet">
<style>
  :root{
    --biotin:#982a31;
    --coq10:#e57d2b;
    --hsn:#c05c97;
    --probiotic:#5aa23a;
    --ink:#1a1a1a;
    --paper:#ffffff;
    --silver-a:#c9c9c9;
    --silver-b:#f1f1f1;
    --badge:#8a8a8a;
  }
  html,body{margin:0;padding:0;overflow:hidden}
  body{width:1200px;height:1200px;background:var(--paper);position:relative;font-family:"Arimo",Arial,sans-serif;color:var(--ink)}
  .label{position:absolute;width:539px;height:258px;background:var(--paper);outline:0.6px solid #bbb;overflow:hidden}
  .label--biotin{left:51px;top:171px;--accent:var(--biotin)}
  .label--coq10{left:617px;top:171px;--accent:var(--coq10)}
  .label--hsn{left:51px;top:514px;--accent:var(--hsn)}
  .label--probiotic{left:617px;top:514px;--accent:var(--probiotic)}

  .top-strip{position:absolute;left:0;top:0;width:100%;height:10px;background:linear-gradient(90deg,var(--silver-a),var(--silver-b) 50%,var(--silver-a))}
  .base-band{position:absolute;left:0;bottom:0;width:100%;height:20px;background:var(--accent)}
  .center-panel{position:absolute;left:166px;top:95px;width:206px;height:163px}
  .center-panel svg{display:block}

  .brand{position:absolute;left:166px;top:26px;width:206px;text-align:center;font-family:"Montserrat",sans-serif;font-weight:700;font-size:17px;color:var(--accent);letter-spacing:0.5px}
  .brand-square{display:inline-block;width:8px;height:8px;background:var(--accent);margin-right:6px;vertical-align:middle}

  .product-title{position:absolute;left:166px;width:206px;text-align:center;color:#fff;font-family:"Montserrat",sans-serif;font-weight:800;line-height:1}
  .pill{position:absolute;left:212px;width:115px;height:14px;border-radius:2px;background:linear-gradient(90deg,var(--silver-a),var(--silver-b) 50%,var(--silver-a));color:var(--accent);text-align:center;font-family:"Montserrat",sans-serif;font-weight:700;font-size:10px;line-height:14px;letter-spacing:0.5px}

  .usage{position:absolute;left:11px;top:26px;width:142px;font-size:5.7px;line-height:1.18}
  .usage p{margin:0 0 4px}
  .usage b{font-weight:700}
  .warnings{position:absolute;left:12px;font-size:5.4px;line-height:1.4;font-weight:700;text-transform:uppercase}
  .disclaimer{position:absolute;left:12px;width:128px;border:0.8px solid var(--ink);padding:2px 3px;font-size:5.2px;line-height:1.05}
  .lot{position:absolute;left:16px;font-size:4.8px;line-height:1.3;width:120px}

  .facts{position:absolute;left:391px;top:35px;width:127px;border:1.4px solid var(--ink);padding:3px 3px 2px;font-size:5.6px}
  .facts h2{margin:0;font-family:"Arimo",sans-serif;font-size:13px;font-weight:700;line-height:1.1}
  .facts .serving{font-size:6.8px;line-height:1.25;border-bottom:3px solid var(--ink);padding-bottom:2px;margin-bottom:1px}
  .facts table{width:100%;border-collapse:collapse}
  .facts th{font-size:4.8px;font-weight:700;text-align:right;padding:2px 0;border-bottom:1px solid var(--ink)}
  .facts td{font-size:4.6px;padding:1px 0;border-bottom:0.4px solid #888}
  .facts td.num{text-align:right}
  .facts .note{font-size:4.4px;padding-top:1px}
  .inactive{position:absolute;left:391px;top:113px;width:140px;font-size:5.4px;line-height:1.2}
  .distributed{position:absolute;left:391px;top:149px;width:130px;text-align:center;font-size:6.6px;font-weight:700}

  .badges{position:absolute;left:411px;top:207px;width:104px;height:24px}
  .badge{position:absolute;top:0;border:0.8px solid var(--badge);border-radius:2px}
  .badge--origin{left:0;width:22px;height:22px;background:#e7e7e7}
  .badge--registry{left:32px;width:40px;height:22px;background:#d7d7d7}
  .badge--recycle{left:81px;width:21px;height:22px}

  /* hair skin nails specifics */
  .facts--hsn{left:383px;top:24px;width:110px;height:200px;font-size:4.4px;padding:2px 3px}
  .facts--hsn h2{font-size:10px}
  .facts--hsn .serving{font-size:3.8px;border-bottom-width:2.5px}
  .facts--hsn td{font-size:3.6px;padding:0.8px 0}
  .facts--hsn th{font-size:3.8px}
  .blend{font-size:3.4px;font-style:italic;line-height:1.25;padding:1px 0 3px;border-bottom:2px solid var(--ink)}
  .side-text{position:absolute;left:500px;top:228px;transform-origin:0 0;transform:rotate(-90deg);width:200px;font-size:5.4px;line-height:1.2}
  .side-dist{position:absolute;left:519px;top:228px;transform-origin:0 0;transform:rotate(-90deg);font-size:6.4px;font-weight:700}
  .badges--vertical{left:515px;top:40px;width:24px;height:104px}
  .badges--vertical .badge{left:0}
  .badges--vertical .badge--recycle{top:0;width:20px;height:20px}
  .badges--vertical .badge--registry{top:30px;width:20px;height:38px}
  .badges--vertical .badge--origin{top:76px;width:20px;height:22px}

  .probiotic-note{font-size:4.6px;line-height:1.25}
</style>
</head>
<body>

<!-- BIOTIN -->
<section class="label label--biotin">
  <div class="top-strip"></div>
  <div class="usage">
    <p><b>SUGGESTED USE:</b> As a dietary supplement take one (1) veggie capsule twice a day. For best results take 20-30 min before a meal with an 8oz. glass of water or as directed by your healthcare professional.</p>
    <p><b>CAUTION:</b> Do not exceed recommended dose. Pregnant or nursing mothers, children under the age of 18, and individuals with a known medical condition should consult a physician before using this or any dieatry supplement.</p>
  </div>
  <div class="warnings" style="top:123px">Keep out the reach of children<br>Do not use if safety seal is<br>damaged or missing.<br>Store in a cool, dry place.</div>
  <div class="disclaimer" style="top:166px">*These statements have not been evaluated by the Food and Drug Administration. This product is not intended to diagnose, treat, cure, or prevent any disease.</div>
  <div class="lot" style="top:214px">Lot # and Expiration Date Printed on bottom of Bottle</div>
  <div class="brand"><span class="brand-square"></span>Vela Norvina</div>
  <div class="center-panel">
    <svg width="206" height="163" viewBox="0 0 206 163">
      <path d="M0 14 C50 -4 110 30 206 0 L206 163 L0 163Z" fill="var(--accent)" opacity="0.35"/>
      <path d="M0 24 C60 6 120 36 206 8 L206 163 L0 163Z" fill="var(--accent)"/>
    </svg>
  </div>
  <div class="product-title" style="top:160px;font-size:35px;letter-spacing:1px">BIOTIN</div>
  <div class="pill" style="top:202px">100% PURE</div>
  <div class="facts">
    <h2>Supplement Facts</h2>
    <div class="serving"><b>Serving Size:</b> 1 Veggie Capsule<br><b>Serving Per Container:</b> 60</div>
    <table>
      <tr><th colspan="2">Amount Per Serving</th><th>%DV</th></tr>
      <tr><td>Biotin</td><td class="num">10,000mcg</td><td class="num">3,333%</td></tr>
      <tr><td>Calcium (as Calcium Carbonate)</td><td class="num">176mg</td><td class="num">18%</td></tr>
    </table>
  </div>
  <div class="inactive">Inactive Ingredients: Cellulose (Vegetable Capsule) Rice Flour, Magnesuim Stearate (vegetable).</div>
  <div class="distributed">Distributed By:</div>
  <div class="badges"><div class="badge badge--origin"></div><div class="badge badge--registry"></div><div class="badge badge--recycle"></div></div>
  <div class="base-band"></div>
</section>

<!-- COQ10 -->
<section class="label label--coq10">
  <div class="top-strip"></div>
  <div class="usage">
    <p><b>SUGGESTED USE:</b> As a dietary supplement take one (1) capsule twice a day. For best results take 20-30 min before a meal with an 8oz. glass of water or as directed by your healthcare professional.</p>
    <p><b>CAUTION:</b> Do not exceed recommended dose. Pregnant or nursing mothers, children under the age of 18, and individuals with a known medical condition should consult a physician before using this or any dieatry supplement.</p>
  </div>
  <div class="warnings" style="top:123px">Keep out the reach of children<br>Do not use if safety seal is<br>damaged or missing.<br>Store in a cool, dry place.</div>
  <div class="disclaimer" style="top:166px">*These statements have not been evaluated by the Food and Drug Administration. This product is not intended to diagnose, treat, cure, or prevent any disease.</div>
  <div class="lot" style="top:214px">Lot # and Expiration Date Printed on bottom of Bottle</div>
  <div class="brand"><span class="brand-square"></span>Vela Norvina</div>
  <div class="center-panel">
    <svg width="206" height="163" viewBox="0 0 206 163">
      <path d="M0 14 C50 -4 110 30 206 0 L206 163 L0 163Z" fill="var(--accent)" opacity="0.35"/>
      <path d="M0 24 C60 6 120 36 206 8 L206 163 L0 163Z" fill="var(--accent)"/>
    </svg>
  </div>
  <div class="product-title" style="top:160px;font-size:35px;letter-spacing:2px">COQ10</div>
  <div class="pill" style="top:202px">UBIQUINONE</div>
  <div class="facts">
    <h2>Supplement Facts</h2>
    <div class="serving"><b>Serving Size:</b> 1 Capsule<br><b>Serving Per Container:</b> Any Count</div>
    <table>
      <tr><th colspan="2">Amount Per Serving</th><th>%DV</th></tr>
      <tr><td>Coenzyme Q- 10 (Ubiquinone)</td><td class="num">200mg</td><td class="num">**</td></tr>
      <tr><td colspan="3" class="note">**Daily Value (DV) not established</td></tr>
    </table>
  </div>
  <div class="inactive">Inactive Ingredients: Cellulose (Vegetable Capsule) Rice Bran.</div>
  <div class="distributed">Distributed By:</div>
  <div class="badges"><div class="badge badge--origin"></div><div class="badge badge--registry"></div><div class="badge badge--recycle"></div></div>
  <div class="base-band"></div>
</section>

<!-- HAIR SKIN NAILS -->
<section class="label label--hsn">
  <div class="top-strip"></div>
  <div class="usage">
    <p><b>SUGGESTED USE:</b> For adults only. Take two (2) capsules a day with food. Do not take this supplement within one hour of taking medications. Do not exceed the recommended dose.</p>
    <p><b>CAUTION:</b> <i>Women who are pregnant or lactating and anyone taking medications should consult a health care professional before using any nutrition product. If ant adverse reactions occur, discontinue use and consult a health care proffesional.</i></p>
  </div>
  <div class="warnings" style="top:100px">Keep out the reach of children<br>Do not use if safety seal is<br>damaged or missing.<br>Store in a cool, dry place.</div>
  <div class="usage" style="top:130px">
    <p><b>IRON WARNING:</b> Accidental overdose of iron containing products is a leading cause of fatal poisoning in children under six (6)</p>
    <p><b>KEEP OUT THE REACH OF CHILDREN.</b> In case of accidental overdose, call a doctor or poison control center immediately.</p>
  </div>
  <div class="disclaimer" style="top:180px">*These statements have not been evaluated by the Food and Drug Administration. This product is not intended to diagnose, treat, cure, or prevent any disease.</div>
  <div class="brand"><span class="brand-square"></span>Vela Norvina</div>
  <div class="center-panel">
    <svg width="206" height="163" viewBox="0 0 206 163">
      <path d="M0 14 C50 -4 110 30 206 0 L206 163 L0 163Z" fill="var(--accent)" opacity="0.35"/>
      <path d="M0 24 C60 6 120 36 206 8 L206 163 L0 163Z" fill="var(--accent)"/>
    </svg>
  </div>
  <div class="product-title" style="top:153px;font-size:22px">HAIR,<br>SKIN &amp; NAILS</div>
  <div class="pill" style="top:210px">ESSENTIALS</div>
  <div class="facts facts--hsn">
    <h2>Supplement Facts</h2>
    <div class="serving"><b>Serving Size:</b> 2 Capsules<br><b>Servings Per Container:</b> Any Count</div>
    <table>
      <tr><th colspan="2">Amount Per Serving</th><th>%DV</th></tr>
      <tr><td>Vitamin A</td><td class="num">2400 IU</td><td class="num">48%</td></tr>
      <tr><td>Vitamin C</td><td class="num">120 mg</td><td class="num">200%</td></tr>
      <tr><td>Calcium Carbonate</td><td class="num">80 mg</td><td class="num">1%</td></tr>
      <tr><td>Iron Ferrous Fumarate</td><td class="num">14.5 mg</td><td class="num">80%</td></tr>
      <tr><td>Vitamin D3</td><td class="num">800 IU</td><td class="num">200%</td></tr>
      <tr><td>Vitamin E</td><td class="num">30 IU</td><td class="num">100%</td></tr>
      <tr><td>Vitamin B1</td><td class="num">6 mg</td><td class="num">400%</td></tr>
      <tr><td>Vitamin B6</td><td class="num">8 mg</td><td class="num">400%</td></tr>
      <tr><td>Folic Acid</td><td class="num">880 ug</td><td class="num">220%</td></tr>
      <tr><td>Vitamin B12</td><td class="num">12 ug</td><td class="num">200%</td></tr>
      <tr><td>Biotin</td><td class="num">600 ug</td><td class="num">200%</td></tr>
      <tr><td>Vitamin B5</td><td class="num">30 mg</td><td class="num">300%</td></tr>
      <tr><td>Magnesium Oxide</td><td class="num">120 mg</td><td class="num">30%</td></tr>
      <tr><td>Zinc oxide</td><td class="num">7.2mg</td><td class="num">48%</td></tr>
      <tr><td>Manganese chelate</td><td class="num">4 mg</td><td class="num">200%</td></tr>
      <tr><td>Potassium gluconate</td><td class="num">12mg</td><td class="num">1%</td></tr>
      <tr><td>Proprietary Blend:</td><td class="num">409 mg</td><td class="num">**</td></tr>
    </table>
    <div class="blend">PABA, L-Tyrosine, Horsetail extract, Fo-Ti, Bamboo extract, Nettle root, Peony, Spirulina, Saw palmetto, Plant sterols, Alfalfa, Barley grass</div>
    <div class="note">** Daily Value (DV) Not Established</div>
  </div>
  <div class="side-text"><b>Inactive Ingredients:</b> Cellulose (Vegetable Capsule), Rice Flour, Magnesium stearate, Silicon dioxide.</div>
  <div class="side-dist">Distributed By:</div>
  <div class="badges badges--vertical"><div class="badge badge--recycle"></div><div class="badge badge--registry"></div><div class="badge badge--origin"></div></div>
  <div class="base-band"></div>
</section>

<!-- PROBIOTIC -->
<section class="label label--probiotic">
  <div class="top-strip"></div>
  <div class="usage" style="left:13px;width:145px">
    <p><b>SUGGESTED USE:</b> As a dietary supplement take two (2) capsules once daily. For best results, take one (1) capsule during the day and one (1) capsule in the evening. Repeat the process daily. Do not exceed two capsules per day.</p>
    <p>Probiotic-40 offers a balanced spectrum of live organisms. Probiotic bacteria are critical for healthy digestion, help maintain the integrity of the intestinal lining, support proper intestinal motility and participate in the detoxification process.*</p>
  </div>
  <div class="warnings" style="top:104px;left:13px">Keep out the reach of children.<br>Do not use if safety seal is<br>damaged or missing.<br>Store in a cool, dry place.</div>
  <div class="disclaimer" style="top:135px;left:13px">*These statements have not been evaluated by the Food and Drug Administration. This product is not intended to diagnose, treat, cure, or prevent any disease.</div>
  <div class="lot" style="top:174px;left:12px">Lot # and Expiration Date Printed on bottom of Bottle</div>
  <div class="lot" style="top:188px;left:75px;font-size:5.4px">V6RO</div>
  <div class="lot probiotic-note" style="top:196px;left:12px;width:142px">This product is formulated with 40 billion CFU per 2 caps and to deliver a minimum potency of 20 billion CFU per 2 caps through the best by date.</div>
  <div class="brand"><span class="brand-square"></span>Vela Norvina</div>
  <div class="center-panel">
    <svg width="206" height="163" viewBox="0 0 206 163">
      <path d="M0 14 C50 -4 110 30 206 0 L206 163 L0 163Z" fill="var(--accent)" opacity="0.35"/>
      <path d="M0 24 C60 6 120 36 206 8 L206 163 L0 163Z" fill="var(--accent)"/>
    </svg>
  </div>
  <div class="product-title" style="top:152px;font-size:20px;line-height:1.05">PROBIOTIC-40<br>40 BILLION</div>
  <div class="product-title" style="top:193px;font-size:11px;font-weight:600">VANTREL<sup style="font-size:5px">®</sup></div>
  <div class="pill" style="top:209px;font-weight:600">Bi-Pass Technology</div>
  <div class="facts" style="top:35px">
    <h2>Supplement Facts</h2>
    <div class="serving"><b>Serving Size:</b> 1 Veggie Capsule<br><b>Serving Per Container:</b> 60</div>
    <table>
      <tr><th colspan="2">Amount Per Serving</th><th>%DV</th></tr>
      <tr><td>Biotin</td><td class="num">10,000mcg</td><td class="num">3,333%</td></tr>
      <tr><td>Calcium (as Calcium Carbonate)</td><td class="num">176mg</td><td class="num">18%</td></tr>
    </table>
  </div>
  <div class="inactive">Incative Ingredients: Cellulose (Vegetable Capsule) Rice Flour, Magnesuim Stearate (vegetable).</div>
  <div class="distributed">Distributed By:</div>
  <div class="badges"><div class="badge badge--origin"></div><div class="badge badge--registry"></div><div class="badge badge--recycle"></div></div>
  <div class="base-band"></div>
</section>

</body>
</html>
```